Commercial janitorial cleaning

Janitorial cleaning particularly for commercial buildings. Website needs to specify free estimates. Location of service is Millbrook, Cedar Falls, North Ridge, Eastport, Lakeview area. Services page with Janitorial services- General Office Cleaning, Construction Cleaning, Carpet Extraction, Consultation/Business, Lighting Maintenance, Seasonal Deep Cleaning, Window cleaning, Event Cleaning, Floor and Carpet Cleaning, Floor Striping and Waxing. Contact us page with email phone number on page and a request page that emails me if they have any questions. About us page-the picture of my family on it with a section I can type a story myself.

Target Market(s)

Commercial businesses

Industry/Entity Type

Janitorial Service

Number of Pages Required

4 page

Font styles to use
Serif
Sans Serif
Script

Colors
ec1f27
1b1b1b
ffffff
9d9d9d

Requirements
Must have
• Phone number 555-314-2760. Must have free estimates on home page. Going for industrial / modern look to website
Nice to have
• Logo is a red and black building so if those colors could be coordinated to website that would be awesome.

```html
<!DOCTYPE html>
<html lang="en">
<head>
<meta charset="utf-8">
<title>Brightline Cleaning – Commercial Janitorial Services</title>
<link rel="stylesheet" href="https://fonts.googleapis.com/css2?family=Montserrat:wght@300;400;500;600;700&family=Oswald:wght@400;500&display=swap">
<style>
:root{
  --red:#ec1f27;
  --dark:#1b1b1b;
  --darker:#141414;
  --white:#ffffff;
  --grey:#9d9d9d;
  --text:#555555;
  --line:#dddddd;
}
*{box-sizing:border-box;margin:0;padding:0}
html,body{width:1200px;height:2261px;overflow:hidden;background:var(--white);font-family:'Montserrat',sans-serif;color:var(--text)}
.page{position:relative;width:1200px;height:2261px}

/* header */
.site-header{position:absolute;left:0;top:0;width:1200px;height:80px;background:var(--dark);z-index:5}
.brand{position:absolute;left:155px;top:15px;width:82px;height:97px;background:var(--white);display:flex;flex-direction:column;align-items:center;justify-content:center;gap:8px;box-shadow:0 2px 6px rgba(0,0,0,.25)}
.brand-mark{width:26px;height:26px;background:var(--red)}
.brand-name{font-size:11px;font-weight:700;color:var(--red);text-align:center;line-height:1.2}
.main-nav a{position:absolute;top:31px;font-size:13px;color:var(--white);text-decoration:none}
.main-nav a.active{color:var(--red)}
.main-nav .active-bar{position:absolute;left:307px;top:54px;width:38px;height:2px;background:var(--red)}
.header-call{position:absolute;left:687px;top:24px;font-family:'Oswald',sans-serif;font-size:21px;color:#d8d8d8;display:flex;align-items:center;gap:6px}
.header-call svg{width:16px;height:18px}
.btn-estimate{position:absolute;left:892px;top:24px;width:151px;height:32px;background:var(--red);color:var(--white);font-size:11px;font-weight:700;letter-spacing:.5px;display:flex;align-items:center;justify-content:center}

/* hero */
.hero{position:absolute;left:0;top:80px;width:1200px;height:478px}
.hero-photo{position:absolute;inset:0;background:linear-gradient(100deg,#6c6a66 0%,#8a8580 35%,#5a5550 60%,#7b746c 80%,#5b5550 100%)}
.hero-photo::after{content:"";position:absolute;inset:0;background:rgba(0,0,0,.25)}
.hero-frame{position:absolute;left:157px;top:149px;width:2px;height:171px;background:rgba(255,255,255,.8)}
.hero-frame::before,.hero-frame::after{content:"";position:absolute;left:0;width:14px;height:2px;background:rgba(255,255,255,.8)}
.hero-frame::before{top:0}.hero-frame::after{bottom:0}
.hero-copy{position:absolute;left:170px;width:404px;text-align:center;color:var(--white)}
.hero-kicker{top:150px;font-size:28px;font-weight:400}
.hero-title{top:183px;font-size:48px;font-weight:700}
.hero-sub{top:236px;font-size:19px;font-weight:400}
.btn-outline{position:absolute;display:flex;align-items:center;justify-content:center;border:2px solid var(--red);color:var(--white);font-size:11px;font-weight:700;letter-spacing:.5px}
.hero .btn-outline{left:300px;top:289px;width:143px;height:30px}
.slide-arrow{position:absolute;width:26px;height:28px}

.estimate-form{position:absolute;left:764px;top:33px;width:279px;height:412px;background:rgba(235,235,235,.9)}
.estimate-form h2{height:57px;background:var(--red);color:var(--white);font-size:19px;font-weight:500;text-align:center;line-height:22px;padding-top:6px}
.field{position:absolute;left:24px;width:233px;height:33px;background:var(--white);border:1px solid #d6d6d6;font-size:10px;color:#a5a5a5;padding:10px 12px}
.field.message{height:113px}
.btn-send{position:absolute;left:24px;top:357px;width:97px;height:30px;background:var(--red);color:var(--white);font-size:11px;font-weight:700;display:flex;align-items:center;justify-content:center;gap:6px}

/* services */
.section-title{position:absolute;left:0;width:1200px;text-align:center;font-size:37px;font-weight:300;color:#222}
.section-sub{position:absolute;left:0;width:1200px;text-align:center;font-size:13px;color:#8a8a8a}
.service-card{position:absolute;top:731px;width:296px;height:223px;text-align:center}
.service-card.featured{background:var(--red);color:var(--white)}
.service-card svg{position:absolute;left:119px;top:26px;width:58px;height:58px}
.service-card h3{position:absolute;left:0;top:96px;width:296px;font-size:14px;font-weight:600;color:#111}
.service-card p{position:absolute;left:22px;top:121px;width:252px;font-size:12px;line-height:16.5px;color:#9a9a9a}
.service-card.featured h3,.service-card.featured p{color:var(--white)}
.service-card .rule{position:absolute;left:126px;top:198px;width:44px;height:1px;background:#bbb}
.service-card.featured .rule{background:var(--white)}

/* welcome */
.welcome{position:absolute;left:0;top:1036px;width:1200px;height:399px;background:var(--dark)}
.welcome h2{position:absolute;left:155px;top:63px;font-size:30px;font-weight:400;color:var(--white)}
.welcome p{position:absolute;left:155px;width:533px;font-size:12px;line-height:17.3px;color:#c9c9c9}
.welcome .btn-outline{left:155px;top:297px;width:145px;height:31px}
.family-photo{position:absolute;left:752px;top:0;width:291px;height:399px;background:linear-gradient(160deg,#6d7b4a 0%,#4d6235 45%,#6b7d86 70%,#3f4a3a 100%)}

/* testimonials */
.testimonial{position:absolute;top:1605px;width:253px;height:253px;border-radius:50%;border:1px solid #e4e4e4;text-align:center;background:var(--white)}
.testimonial.featured{border:none;box-shadow:0 6px 22px rgba(0,0,0,.14)}
.quote-mark{position:absolute;left:0;top:36px;width:253px;font-size:62px;font-weight:700;color:var(--red);line-height:62px}
.testimonial blockquote{position:absolute;left:-10px;top:92px;width:273px;font-size:13px;line-height:21px;color:#8c8c8c;white-space:nowrap}
.testimonial .name{position:absolute;left:0;top:178px;width:253px;font-size:14px;font-weight:600;color:#111}
.testimonial .role{position:absolute;left:0;top:198px;width:253px;font-size:12px;color:#999}

/* footer */
.site-footer{position:absolute;left:0;top:1924px;width:1200px;height:288px;background:var(--dark);color:#bdbdbd}
.footer-col h3{position:absolute;top:41px;font-size:18px;font-weight:400;color:var(--white)}
.footer-divider{position:absolute;top:43px;width:1px;height:196px;background:#444}
.footer-text{position:absolute;font-size:12px;line-height:17px;color:#bdbdbd}
.footer-call{position:absolute;left:155px;top:147px;font-family:'Oswald',sans-serif;font-size:19px;color:var(--white);display:flex;align-items:center;gap:5px}
.footer-call svg{width:15px;height:16px}
.social{position:absolute;top:207px;width:28px;height:28px;border-radius:50%;border:1px solid var(--red)}
.social.active{background:var(--red)}
.newsletter-input{position:absolute;left:535px;top:115px;width:281px;height:33px;background:#2a2a2a;border-bottom:1px solid #555;font-size:12px;color:#ddd;padding:9px 15px}
.btn-newsletter{position:absolute;left:535px;top:172px;width:97px;height:31px;border:2px solid var(--red);color:var(--white);font-size:11px;font-weight:700;display:flex;align-items:center;justify-content:center;gap:6px}
.quick-links li{position:absolute;left:915px;list-style:none;font-size:13px;color:#bdbdbd}
.quick-links li::before{content:"›";margin-right:7px}
.quick-links li.active{color:var(--red)}
.bottom-bar{position:absolute;left:0;top:2212px;width:1200px;height:49px;background:var(--darker)}
.copyright{position:absolute;left:155px;top:16px;font-size:12px;color:#9d9d9d}
.to-top{position:absolute;left:1026px;top:16px;width:16px;height:18px}
</style>
</head>
<body>
<div class="page">

<header class="site-header">
  <div class="brand"><span class="brand-mark"></span><span class="brand-name">Brightline<br>Cleaning</span></div>
  <nav class="main-nav">
    <a class="active" style="left:307px">Home</a>
    <span class="active-bar"></span>
    <a style="left:387px">About Us</a>
    <a style="left:487px">Services</a>
    <a style="left:580px">Contact Us</a>
  </nav>
  <div class="header-call">Call Us
    <svg viewBox="0 0 16 18"><path d="M4 1h3l1 4-2 1.5c1 2.5 2.5 4 5 5L12.5 9.5l3.5 1v3.5c0 1-1 2-2 2C7 16 1 10 1 3c0-1 1-2 3-2z" fill="#ec1f27"/></svg>
    555-314-2760</div>
  <div class="btn-estimate">FREE ESTIMATES</div>
</header>

<section class="hero">
  <div class="hero-photo" role="img" aria-label="Worker vacuuming the carpet of a bright modern office lobby"></div>
  <div class="hero-frame"></div>
  <div class="hero-copy hero-kicker">We Do The Cleaning</div>
  <div class="hero-copy hero-title">Work For You</div>
  <div class="hero-copy hero-sub">Cleaning Services</div>
  <div class="btn-outline">EXPLORE MORE</div>
  <svg class="slide-arrow" style="left:81px;top:226px" viewBox="0 0 26 28"><path d="M8 1h17v26H8v-8M8 9V1" fill="none" stroke="#fff" stroke-width="2"/><path d="M18 14H2M8 8l-6 6 6 6" fill="none" stroke="#fff" stroke-width="2"/></svg>
  <svg class="slide-arrow" style="left:1094px;top:226px" viewBox="0 0 26 28"><path d="M18 1H1v26h17v-8M18 9V1" fill="none" stroke="#ec1f27" stroke-width="2"/><path d="M8 14h16M18 8l6 6-6 6" fill="none" stroke="#ec1f27" stroke-width="2"/></svg>

  <form class="estimate-form">
    <h2>Get Your<br>Free Estimates</h2>
    <div class="field" style="top:83px">Name</div>
    <div class="field" style="top:128px">Email</div>
    <div class="field" style="top:173px">Phone</div>
    <div class="field message" style="top:220px">Message ...</div>
    <div class="btn-send"><svg width="11" height="11" viewBox="0 0 11 11"><path d="M0 5l11-5-4 11-2-4z" fill="#fff"/></svg>SEND</div>
  </form>
</section>

<section class="services">
  <h2 class="section-title" style="top:614px">Our Services</h2>
  <p class="section-sub" style="top:667px">Location of service is Millbrook, Cedar Falls, North Ridge, Eastport, Lakeview area.</p>
  <svg class="slide-arrow" style="left:80px;top:836px" viewBox="0 0 26 28"><path d="M8 1h17v26H8v-8M8 9V1" fill="none" stroke="#999" stroke-width="2"/><path d="M18 14H2M8 8l-6 6 6 6" fill="none" stroke="#999" stroke-width="2"/></svg>
  <svg class="slide-arrow" style="left:1094px;top:836px" viewBox="0 0 26 28"><path d="M18 1H1v26h17v-8M18 9V1" fill="none" stroke="#ec1f27" stroke-width="2"/><path d="M8 14h16M18 8l6 6-6 6" fill="none" stroke="#ec1f27" stroke-width="2"/></svg>

  <article class="service-card" style="left:153px">
    <svg viewBox="0 0 58 58" fill="none" stroke="#111" stroke-width="2"><rect x="16" y="8" width="26" height="46"/><path d="M6 54h46M12 54V30h4M46 54V34h-4"/><path d="M21 14h4M29 14h4M21 21h4M29 21h4M21 28h4M29 28h4M21 35h4M29 35h4M21 42h4M29 42h4M37 14h1M37 21h1"/></svg>
    <h3>General Office Cleaning</h3>
    <p>Contrary to popular belief, Lorem Ipsum is not simply random must explain to you how all this mistaken...</p>
    <span class="rule"></span>
  </article>
  <article class="service-card featured" style="left:452px">
    <svg viewBox="0 0 58 58" fill="none" stroke="#fff" stroke-width="2"><rect x="4" y="22" width="16" height="32"/><rect x="20" y="6" width="18" height="48"/><rect x="38" y="18" width="16" height="36"/><path d="M9 29h6M9 36h6M9 43h6M25 13h8M25 20h8M25 27h8M25 34h8M25 41h8M43 25h6M43 32h6M43 39h6M26 54v-7h6v7"/></svg>
    <h3>Construction Cleaning</h3>
    <p>Contrary to popular belief, Lorem Ipsum is not simply random must explain to you how all this mistaken...</p>
    <span class="rule"></span>
  </article>
  <article class="service-card" style="left:749px">
    <svg viewBox="0 0 58 58" fill="none" stroke="#111" stroke-width="2"><rect x="8" y="4" width="42" height="50"/><rect x="13" y="9" width="32" height="36"/><path d="M29 9v36M13 27h32M6 54h46"/></svg>
    <h3>Window cleaning</h3>
    <p>Contrary to popular belief, Lorem Ipsum is not simply random must explain to you how all this mistaken...</p>
    <span class="rule"></span>
  </article>
</section>

<section class="welcome">
  <h2>Welcome</h2>
  <p style="top:110px">There are many variations of passages of Lorem Ipsum available, but the majority There are many variations of passages of Lorem Ipsum available, but the majority have suffered alteration in some form, by injected humour, or randomised words which don't look even slightly believable. If you are going to use.</p>
  <p style="top:197px">a passage of Lorem Ipsum, you need to be sure there isn't anything embarrassing hidden in the middle of text. All the Lorem Ipsum generators on the Internet tend to repeat predefined chunks as necessary, making this the first true generator on the Internet. It uses a dictionary of over 200 Latin words, combined...</p>
  <div class="btn-outline">DISCOVER MORE</div>
  <div class="family-photo" role="img" aria-label="Family portrait on a wooden ladder in a garden"></div>
</section>

<section class="testimonials">
  <h2 class="section-title" style="top:1490px">Testimonials</h2>
  <p class="section-sub" style="top:1543px">Always Have Something Nice To Say About Us</p>
  <svg class="slide-arrow" style="left:80px;top:1717px" viewBox="0 0 26 28"><path d="M8 1h17v26H8v-8M8 9V1" fill="none" stroke="#999" stroke-width="2"/><path d="M18 14H2M8 8l-6 6 6 6" fill="none" stroke="#999" stroke-width="2"/></svg>
  <svg class="slide-arrow" style="left:1094px;top:1717px" viewBox="0 0 26 28"><path d="M18 1H1v26h17v-8M18 9V1" fill="none" stroke="#ec1f27" stroke-width="2"/><path d="M8 14h16M18 8l6 6-6 6" fill="none" stroke="#ec1f27" stroke-width="2"/></svg>

  <article class="testimonial" style="left:170px">
    <span class="quote-mark">“</span>
    <blockquote>It is a long established fact that a<br>reader will be distracted by the read-<br>able content of a page.</blockquote>
    <div class="name">Nora Bell</div><div class="role">Master-builder</div>
  </article>
  <article class="testimonial featured" style="left:472px">
    <span class="quote-mark">“</span>
    <blockquote>It is a long established fact that a<br>reader will be distracted by the read-<br>able content of a page.</blockquote>
    <div class="name">Victor Lane</div><div class="role">Master-builder</div>
  </article>
  <article class="testimonial" style="left:775px">
    <span class="quote-mark">“</span>
    <blockquote>It is a long established fact that a<br>reader will be distracted by the read-<br>able content of a page.</blockquote>
    <div class="name">Irene Cole</div><div class="role">Master-builder</div>
  </article>
</section>

<footer class="site-footer">
  <div class="footer-col"><h3 style="left:155px">Contact Us</h3></div>
  <p class="footer-text" style="left:155px;top:88px">Brightline Cleaning<br>4410 Meridian Park Blvd Fairhaven,<br>OR 97412</p>
  <div class="footer-call">Call Us
    <svg viewBox="0 0 16 18"><path d="M4 1h3l1 4-2 1.5c1 2.5 2.5 4 5 5L12.5 9.5l3.5 1v3.5c0 1-1 2-2 2C7 16 1 10 1 3c0-1 1-2 3-2z" fill="#ec1f27"/></svg>
    555-314-2760</div>
  <p class="footer-text" style="left:155px;top:177px">info@brightlinecleaning.com</p>
  <span class="social" style="left:156px"></span>
  <span class="social active" style="left:193px"></span>
  <span class="social" style="left:230px"></span>
  <span class="social" style="left:267px"></span>

  <span class="footer-divider" style="left:485px"></span>
  <div class="footer-col"><h3 style="left:535px">Newsletter</h3></div>
  <p class="footer-text" style="left:535px;top:79px">To get the latest scoop right to your inbox.</p>
  <div class="newsletter-input">Enter your email ...</div>
  <div class="btn-newsletter"><svg width="11" height="11" viewBox="0 0 11 11"><path d="M0 5l11-5-4 11-2-4z" fill="#fff"/></svg>SEND</div>

  <span class="footer-divider" style="left:865px"></span>
  <div class="footer-col"><h3 style="left:915px">Quick Link</h3></div>
  <ul class="quick-links">
    <li class="active" style="top:82px">Home</li>
    <li style="top:111px">About Us</li>
    <li style="top:140px">Services</li>
    <li style="top:169px">Contact Us</li>
  </ul>
</footer>

<div class="bottom-bar">
  <p class="copyright">© 2017 Brightline Cleaning Services. All rights reserved.</p>
  <svg class="to-top" viewBox="0 0 16 18"><path d="M8 17V3M2 9l6-6 6 6" fill="none" stroke="#ec1f27" stroke-width="3"/></svg>
</div>

</div>
</body>
</html>
```